Keystone Arc Mentoring

We would like to refresh the design of our current website. We want to make it cleaner, more open and more professional looking using simple page layouts and crisp fonts. The site should be lighter and be easy to navigate.

It is important that it be easy to add and change content.

The current site can be seen at www.keystonearcmentor.example

As part of this, we want our logo colors to be darker blue and green more professional than they are currently. The current logo is attached as you can see the colors are too "neon"

THIS IS A WEBSITE DESIGN REFRESH PROJECT

Target Market(s)

Executives

Industry/Entity Type

Cleaner

Font styles to use
Sans Serif

Colors
0355a3
cfdfed
9bcb3c

Requirements
Must have
• Ease of use, ease of adding content
Should not have
• No crazy colors, not too busy...

```html
<!DOCTYPE html>
<html lang="en">
<head>
<meta charset="utf-8">
<title>Keystone Arc Mentoring</title>
<link href="https://fonts.googleapis.com/css2?family=Open+Sans:ital,wght@0,400;0,600;0,700;1,400;1,600&family=Dancing+Script:wght@500&display=swap" rel="stylesheet">
<style>
:root{
  --blue:#0355a3;
  --blue-dark:#03468a;
  --blue-light:#cfdfed;
  --green:#9bcb3c;
  --ink:#333;
  --muted:#777;
  --panel:#f3f3f3;
  --line:#dcdcdc;
  --bar:#3e3e3e;
}
*{box-sizing:border-box;margin:0;padding:0}
html,body{width:921px;height:1200px;overflow:hidden;background:#fff}
body{font-family:"Open Sans",Arial,sans-serif;color:var(--ink);font-size:11px}
.page{position:relative;width:921px;height:1200px;overflow:hidden;background:#fff}
.top-band{position:absolute;left:0;top:0;width:921px;height:104px;background:linear-gradient(90deg,#0a5fb0,#1f74c4 50%,#0a5fb0)}
.email{position:absolute;right:41px;top:20px;color:#fff;font-size:13.5px;font-weight:600;display:flex;align-items:center;gap:6px}
.brand-card{position:absolute;left:40px;top:7px;width:290px;height:97px}
.brand{position:absolute;left:22px;top:34px;display:flex;align-items:center;gap:8px}
.brand-dot{width:20px;height:20px;border-radius:50%;background:var(--green)}
.brand-name{font-size:19px;font-weight:700;color:var(--blue)}
.tagline{position:absolute;left:22px;top:62px;font-size:6px;letter-spacing:.6px;color:var(--blue);text-transform:uppercase}
.call-bar{position:absolute;left:313px;top:60px;width:567px;height:44px;background:linear-gradient(#5a5a5a,#2e2e2e);border-radius:0 8px 0 0}
.call{position:absolute;left:73px;top:11px;color:#ddd;font-size:16px}
.call b{color:#fff;font-weight:400}
.search{position:absolute;left:310px;top:9px;width:243px;height:25px;border-radius:13px;background:#2a2a2a;border:1px solid #666;color:#bbb;font-style:italic;font-size:10.5px;padding:5px 12px}
.search svg{position:absolute;right:9px;top:5px}
.nav{position:absolute;left:40px;top:105px;width:840px;height:48px;background:#fff;border:1px solid #cfd9e4;border-top:none;border-radius:0 0 6px 6px;display:flex}
.nav a{display:block;height:47px;line-height:44px;padding:0 19px;font-size:15px;color:#555;text-decoration:none;border-right:1px solid #e3e3e3}
.nav a.current{color:#1d2a4a;font-weight:700;border-bottom:4px solid var(--blue)}
.nav a:last-child{border-right:none}
.hero{position:absolute;left:40px;top:154px;width:840px;height:425px;border-radius:6px;background:linear-gradient(180deg,#c9d6e0 0%,#aebdca 45%,#6f7a86 75%,#3b424c 100%)}
.card{position:absolute;top:613px;width:185px;height:288px;border-radius:6px;background:var(--panel);border:1px solid #e3e3e3}
.card.featured{background:#e9f0f8;border-color:#c6d8ec}
.card h3{height:47px;margin:4px 4px 0 7px;padding:13px 0 0 14px;font-size:13.5px;font-weight:400;color:#333;border-left:4px solid #bbb;background:#fafafa}
.card.featured h3{color:var(--blue);border-left-color:var(--blue);background:#f4f8fc}
.card .body{padding:14px 13px 0 13px;font-size:10.8px;line-height:16.5px;color:#555;text-align:justify}
.card em{display:block;color:var(--blue);font-weight:600;margin-bottom:8px;text-align:left;font-size:10.5px}
.card.featured em{color:#222;font-weight:400}
.card p{margin-bottom:6px}
.card ul{list-style:none;margin-top:9px}
.card li{color:var(--blue);font-style:italic;font-size:10.5px;line-height:18.5px}
.card li::before{content:"» ";font-style:normal}
.testimonial{position:absolute;left:637px;top:613px;width:237px;height:214px}
.testimonial .sheet{position:absolute;left:12px;top:10px;width:212px;height:190px;background:#e9e9e9;border:4px solid #fff;box-shadow:0 1px 4px rgba(0,0,0,.3)}
.testimonial h3{position:absolute;left:0;width:100%;top:4px;text-align:center;font-family:"Dancing Script",cursive;font-weight:500;font-size:21px;color:var(--blue)}
.arrow{position:absolute;top:8px;width:15px;height:15px;border-radius:50%;background:#7db43a}
.arrow.prev{left:7px}.arrow.next{right:7px}
.quote{position:absolute;left:10px;top:44px;width:185px;font-size:11px;line-height:15.5px;color:#222}
.author{position:absolute;left:10px;top:132px;color:var(--blue);font-style:italic;font-size:11.5px;line-height:15.5px}
.newsletter{position:absolute;left:640px;top:858px;width:239px;height:212px;border:1px solid var(--blue);border-radius:4px;background:#fff}
.newsletter h3{height:28px;background:var(--blue);color:#fff;font-size:15px;font-weight:600;padding:3px 11px;border-radius:3px 3px 0 0}
.newsletter .field{margin:9px 9px 0 9px;height:27px;border:1px solid #ccc;background:linear-gradient(#fff,#f2f2f2);font-style:italic;font-size:11px;color:#777;padding:5px 7px}
.newsletter .field:first-of-type{margin-top:9px}
.signup{position:absolute;right:-1px;bottom:-1px;width:74px;height:27px;background:var(--blue);color:#fff;font-style:italic;font-size:13px;padding:3px 0 0 18px;clip-path:polygon(10px 0,100% 0,100% 100%,0 100%)}
.welcome{position:absolute;left:40px;top:918px;width:578px}
.welcome h2{font-size:17.5px;font-style:italic;font-weight:600;color:var(--blue);padding-bottom:8px;border-bottom:1px dotted #bbb}
.welcome h2 span{color:var(--green)}
.welcome p{margin-top:13px;font-size:11.2px;line-height:18.4px;color:#777;text-align:justify}
.more{position:absolute;left:40px;top:1049px;width:578px;height:20px;border-bottom:1px solid var(--blue)}
.more span{position:absolute;right:0;bottom:0;width:22px;height:19px;background:var(--blue)}
.footer-nav{position:absolute;left:0;top:1108px;width:921px;height:43px;background:linear-gradient(#ececec,#cfcfcf)}
.footer-nav .links{position:absolute;left:48px;top:14px;font-size:11.3px;color:#555}
.footer-nav .links a{color:#555;text-decoration:none}
.footer-nav .links a.current{color:var(--blue)}
.social{position:absolute;right:48px;top:7px;display:flex;gap:11px}
.social span{width:29px;height:29px;border-radius:50%;background:#9c9c9c;border:2px solid #e0e0e0}
.social span.active{background:var(--blue)}
.footer-base{position:absolute;left:0;top:1151px;width:921px;height:49px;background:linear-gradient(#0b5cab,#064c95);color:#fff;font-size:11.5px;padding:15px 44px}
</style>
</head>
<body>
<div class="page">
  <div class="top-band"></div>
  <div class="email">
    <svg width="20" height="16" viewBox="0 0 20 16"><rect x="1" y="2" width="18" height="13" fill="none" stroke="#fff" stroke-width="2"/><path d="M1 2l9 7 9-7" fill="none" stroke="#fff" stroke-width="2"/></svg>
    info@keystonearcmentor.example
  </div>

  <div class="call-bar">
    <div class="call">Call Now: <b>555 014 2290</b></div>
    <div class="search">Search...
      <svg width="14" height="14" viewBox="0 0 14 14"><circle cx="5.5" cy="5.5" r="4" fill="none" stroke="#9bcb3c" stroke-width="2"/><path d="M8.5 8.5l4 4" stroke="#9bcb3c" stroke-width="2.4"/></svg>
    </div>
  </div>

  <svg class="brand-card" viewBox="0 0 290 97" width="290" height="97"><path d="M0 8Q0 0 8 0H262Q272 0 276 10L290 97H0Z" fill="#fff"/></svg>
  <div class="brand" style="left:62px;top:73px">
    <span class="brand-dot"></span><span class="brand-name">Keystone Arc Mentoring</span>
  </div>
  <div class="tagline" style="left:62px;top:98px">Coaching leaders and companies from distress to success</div>

  <nav class="nav">
    <a class="current" href="#">Home</a>
    <a href="#">About Us</a>
    <a href="#">Why Coaching</a>
    <a href="#">Services</a>
    <a href="#">Clients</a>
    <a href="#">Resources</a>
    <a href="#">Blog</a>
    <a href="#" style="flex:1">Contact Us</a>
  </nav>

  <div class="hero" role="img" aria-label="Photo of a smiling executive team gathered around a glass meeting table in a bright city office"></div>

  <section class="card featured" style="left:40px">
    <h3>Leadership Coaching</h3>
    <div class="body">
      <em>"Everyone has a plan until they get punched in the face."</em>
      <p>The Stream of Consciousness, flows through only a few of the world's best organizations and is fed by creative and positive thinking that produces questions like:</p>
      <ul><li>What's Right?</li><li>What's the opportunity here?</li><li>How can we make this work?"</li></ul>
    </div>
  </section>

  <section class="card" style="left:238px">
    <h3>Assessments</h3>
    <div class="body">
      <em>You Are Here!</em>
      <p>Great coaching relationships start by meeting the client where they are. We use an array of assessment tools, both attitudinal and personality, to establish an effective kickoff point.</p>
      <p>The Core Leadership Index (C.L.I.) is a one-of-a-kind assessment that enables leader</p>
    </div>
  </section>

  <section class="card" style="left:435px">
    <h3>Skills Coaching</h3>
    <div class="body">
      <em>Skills CoachingBuilding Capabilities and Capacity</em>
      <p>Most organizations invest in "training" their employees with the intention of increasing their productivity, their value to the organization, and ultimately the organization's capacity to respond to opportunities and challenges. Too often, this investment is one and done.</p>
    </div>
  </section>

  <aside class="testimonial">
    <svg width="237" height="214" viewBox="0 0 237 214" style="position:absolute;left:0;top:0"><path d="M4 34L214 0 232 192 22 214Z" fill="var(--blue)"/></svg>
    <div class="sheet">
      <span class="arrow prev"></span><span class="arrow next"></span>
      <h3>Client Testimonials</h3>
      <p class="quote">"Keystone Arc Mentoring works with executives at under-performing organizations experiencing a range of issues from mild dysfunction to significant distress. "</p>
      <p class="author">Alan T.<br>CEO Publishing Services Company</p>
    </div>
  </aside>

  <form class="newsletter">
    <h3>Sign up for Newsletter</h3>
    <div class="field">First Name:</div>
    <div class="field">Last Name:</div>
    <div class="field">Company Name:</div>
    <div class="field">Email</div>
    <div class="signup">Sing up</div>
  </form>

  <section class="welcome">
    <h2><span>Welcome to</span> Keystone Arc Mentoring</h2>
    <p>Keystone Arc Mentoring works with executives and companies that are facing issues ranging from mild dysfunction to significant distress. We help them pivot, regain control and achieve renewed growth. Keystone Arc Mentoring employs the Core LeadershipTM process developed by Daniel R. Whitfield PhD., founder of the Academy for Applied Leadership Coaching (AALC). Core LeadershipTM is the process that develops a personally effective style of leadership that positively influences and changes</p>
  </section>
  <div class="more"><span></span></div>

  <footer>
    <div class="footer-nav">
      <div class="links"><a class="current" href="#">Home</a> / <a href="#">About Us</a> / <a href="#">Why coaching</a> / <a href="#">Services</a> / <a href="#">Clients</a> / <a href="#">Resources</a> / <a href="#">Blog</a> / <a href="#">Contact Us</a></div>
      <div class="social"><span class="active"></span><span></span><span></span><span></span></div>
    </div>
    <div class="footer-base">Copyright © 2014 Keystone Arc Mentoring. &nbsp; Terms &nbsp; / &nbsp; Privacy</div>
  </footer>
</div>
</body>
</html>
```